Shift Haven Brochure for on call home care staffing

Brochure to describe Shift haven services. Shift haven provides after hours on-call staffing and scheduling only for home care agencies. We are 100% US Based with real agents in person answering calls. We act as an extension of their agency and integrate seamlessly. I dropped in my attempt at the brochure but my AI images suck. We want realistic images with an Americana feel. I also don't want the gold color or the same images on the new one. Feel free to redo the writing.

Target Market(s)

home care agencies

Industry/Entity Type

Health care staffing

Font styles to use
Serif
Sans Serif

Colors
0054AA
0677BA
7BADD7
CADEEF
E8F1F8

Requirements
Must have
• Catchy headlines
Nice to have
• I'd like to see professional style brochure with squares integrated in.
Should not have
• VIBRANT COLORS

```html
<!DOCTYPE html>
<html lang="en">
<head>
<meta charset="utf-8">
<title>Shift Haven Brochure</title>
<link href="https://fonts.googleapis.com/css2?family=Montserrat:wght@300;400;500;600;700;800&family=Oswald:wght@600;700&display=swap" rel="stylesheet">
<style>
:root{
  --navy:#0054aa;
  --navy-deep:#003f82;
  --blue:#0677ba;
  --sky:#7badd7;
  --ice:#cadeef;
  --paper:#ffffff;
  --mist:#e8f1f8;
  --ink:#1d2a3a;
  --stage:#b9b9b9;
  --photo-a:#cadeef;
  --photo-b:#7badd7;
}
*{box-sizing:border-box;margin:0;padding:0}
html,body{width:706px;height:1200px;overflow:hidden}
body{background:var(--stage);font-family:"Montserrat",Arial,sans-serif;color:var(--ink);position:relative}
.sheet{position:absolute;left:13px;width:680px;height:480px;display:flex;box-shadow:0 6px 18px rgba(0,0,0,.25)}
.sheet--outside{top:60px}
.sheet--inside{top:620px}
.panel{position:relative;width:226.67px;height:100%;overflow:hidden}
.photo{position:absolute;background:linear-gradient(150deg,var(--photo-a),var(--photo-b))}
.block{position:absolute;left:0;right:0}
.navy{background:var(--navy)}
.blue{background:var(--blue)}
.white{background:var(--paper)}
.mist{background:var(--mist)}
.accent{color:var(--ice)}
.rule{height:1px;background:var(--sky);margin:6px 0 8px}
.body-copy{font-size:7px;line-height:1.28;color:#fff;font-weight:400}
.h-section{font-weight:700;font-size:12.5px;letter-spacing:.2px;color:#fff}
.checks{list-style:none}
.checks li{font-size:7.2px;color:#fff;display:flex;align-items:center;gap:5px;margin-bottom:4px}
.checks svg{width:7px;height:7px}
.headline{font-weight:800;font-size:15px;line-height:1.08;color:#fff;text-transform:uppercase}
.contact{font-size:7.4px;color:var(--ink);display:flex;align-items:center;gap:5px;margin-bottom:4px}
.contact svg{width:7px;height:7px}
.call-label{font-weight:800;font-size:17px;color:var(--blue);text-align:center}
.phone{font-family:"Oswald",Arial,sans-serif;font-weight:700;font-size:28px;color:var(--navy-deep);display:flex;align-items:center;justify-content:center;gap:4px;letter-spacing:-.5px}
.phone svg{width:18px;height:20px}
.brand{display:flex;align-items:center;justify-content:center;gap:8px;font-weight:800;color:var(--navy-deep);letter-spacing:1.2px;text-transform:uppercase}
.brand-square{width:14px;height:14px;background:var(--navy)}
.oncall{color:var(--mist);text-transform:uppercase;line-height:.95}
.oncall .thin{font-weight:300;font-size:30px;display:block}
.oncall .bold{font-weight:800;font-size:30px;display:block}
.tagline{display:inline-block;background:var(--navy-deep);color:#fff;font-weight:700;font-size:10px;padding:4px 8px;margin-top:6px}
.service{display:flex;gap:9px;margin-bottom:12px;align-items:center}
.service-icon{width:36px;height:36px;border-radius:50%;border:2px solid #fff;background:var(--blue);flex:none;display:flex;align-items:center;justify-content:center}
.service-icon svg{width:18px;height:18px}
.service h3{font-size:8.6px;font-weight:600;color:#fff;margin-bottom:2px}
.service p{font-size:6.8px;line-height:1.2;color:#fff}
.banner{position:absolute;left:0;width:172px;background:var(--blue);color:#fff;font-weight:800;font-size:15px;line-height:1.05;padding:7px 12px 7px 20px;text-transform:uppercase}
.dark-copy{font-size:6.6px;line-height:1.22;color:var(--ink)}
.strip{position:absolute;bottom:0;height:5px}
</style>
</head>
<body>

<section class="sheet sheet--outside">
  <div class="panel navy">
    <div class="photo" style="left:0;top:0;right:0;height:158px" role="img" aria-label="Photo of a smiling call agent with a headset working at a computer in an office"></div>
    <div class="block blue" style="top:158px;height:146px;padding:9px 14px 0 20px">
      <p class="body-copy">Comprehensive on-call staffing solution designed for home care by home care professionals. Experience seamless scheduling tailored to meet the unique needs of your clients and staff. Our team understands the demands of home care, ensuring that every shift is covered by qualified, compassionate caregivers. We prioritize flexibility and reliability, so you can focus on providing exceptional care while we handle the logistics. Whether you need last-minute coverage or regular scheduling support, our service is here to enhance your operation's efficiency and peace of mind. Let us help you get your weekends back and maintain the high standards your clients deserve.</p>
    </div>
    <div class="block navy" style="top:304px;bottom:0;padding:16px 14px 0 20px">
      <h2 class="h-section">WHY <span class="accent">CHOOSE</span> US</h2>
      <div class="rule" style="width:140px"></div>
      <ul class="checks">
        <li><svg viewBox="0 0 10 10"><circle cx="5" cy="5" r="5" fill="#7badd7"/><path d="M2.6 5.2l1.6 1.5 3.2-3.3" stroke="#0054aa" stroke-width="1.3" fill="none"/></svg>100% US Based</li>
        <li><svg viewBox="0 0 10 10"><circle cx="5" cy="5" r="5" fill="#7badd7"/><path d="M2.6 5.2l1.6 1.5 3.2-3.3" stroke="#0054aa" stroke-width="1.3" fill="none"/></svg>Home care experts</li>
        <li><svg viewBox="0 0 10 10"><circle cx="5" cy="5" r="5" fill="#7badd7"/><path d="M2.6 5.2l1.6 1.5 3.2-3.3" stroke="#0054aa" stroke-width="1.3" fill="none"/></svg>Leading choice in on-call</li>
      </ul>
    </div>
  </div>

  <div class="panel white">
    <div class="block navy" style="top:0;height:108px;padding:20px 14px 0 18px">
      <h1 class="headline">Home care<br>scheduling by<br><span class="accent">people who know<br>home care.</span></h1>
    </div>
    <div class="block white" style="top:108px;height:84px;padding:14px 14px 0 18px">
      <h2 class="h-section" style="color:var(--navy-deep);font-size:11px;line-height:1.1">GET IN TOUCH<br>WITH US</h2>
      <div class="rule" style="width:170px"></div>
      <p class="contact"><svg viewBox="0 0 10 10"><circle cx="5" cy="5" r="5" fill="#0054aa"/><rect x="2.4" y="3.3" width="5.2" height="3.6" fill="none" stroke="#fff" stroke-width=".7"/><path d="M2.4 3.3L5 5.4l2.6-2.1" fill="none" stroke="#fff" stroke-width=".7"/></svg>jordanreyes@shifthavenhomecare.com</p>
      <p class="contact"><svg viewBox="0 0 10 10"><circle cx="5" cy="5" r="5" fill="#0054aa"/><path d="M2.5 5.2L5 2.8l2.5 2.4V7.4H2.5z" fill="#fff"/></svg>Arlington Texas</p>
    </div>
    <div class="photo" style="left:0;top:200px;width:210px;height:128px" role="img" aria-label="Photo of a man with glasses and a headset reviewing a tablet at his desk"></div>
    <div class="block" style="top:344px;text-align:center">
      <p class="call-label">CALL US</p>
      <p class="phone"><svg viewBox="0 0 18 20"><path d="M4 1.5c1-.6 2-.3 2.6.6l1.4 2.6c.4.8.2 1.7-.5 2.2l-1.2.9c.7 2.4 2 4.5 3.9 6.1l1.2-.8c.7-.5 1.6-.4 2.2.2l2 2c.6.7.6 1.7-.1 2.3l-1.2 1c-1 .8-2.4 1-3.6.4C5.5 16.6 2 11.3 1.7 5.4c-.1-1.3.5-2.6 1.5-3.3z" fill="#0677ba"/></svg>817.555.0142</p>
    </div>
    <div class="strip navy" style="left:0;width:112px"></div>
    <div class="strip blue" style="left:118px;right:0"></div>
  </div>

  <div class="panel blue">
    <div class="block mist" style="top:0;height:108px">
      <div style="position:absolute;right:0;top:0;width:22px;height:22px;background:var(--navy)"></div>
      <div style="position:absolute;right:22px;top:28px;width:10px;height:10px;background:var(--sky)"></div>
      <div class="brand" style="position:absolute;left:0;right:0;top:58px;font-size:16px"><span class="brand-square"></span>Shift Haven</div>
    </div>
    <div class="photo" style="left:0;top:108px;right:10px;height:196px" role="img" aria-label="Overhead photo of a team of call agents at computers with a supervisor pointing at a screen"></div>
    <div class="block" style="top:322px;padding:0 14px 0 18px">
      <p class="oncall"><span class="thin">On call</span><span class="bold">Service</span></p>
      <span class="tagline">Get your weekends back</span>
    </div>
  </div>
</section>

<section class="sheet sheet--inside">
  <div class="panel mist">
    <div class="block navy" style="top:0;height:275px;padding:20px 14px 0 20px">
      <h2 class="h-section">OUR <span class="accent">SERVICES</span></h2>
      <div class="rule" style="width:180px;margin-bottom:12px"></div>
      <div class="service">
        <div class="service-icon"><svg viewBox="0 0 20 20"><path d="M4 2.5c.8-.5 1.7-.3 2.2.5l1.2 2.2c.3.7.2 1.4-.4 1.9l-1 .7c.6 2 1.7 3.7 3.3 5.1l1-.7c.6-.4 1.3-.3 1.8.2l1.7 1.7c.5.6.5 1.4-.1 1.9l-1 .8c-.9.7-2 .8-3 .3C5.8 15 2.9 10.6 2.6 5.7c0-1.1.4-2.2 1.4-3.2z" fill="#fff"/><circle cx="14.5" cy="5.5" r="3.3" fill="none" stroke="#fff" stroke-width="1.2"/><path d="M14.5 3.8v3.4M12.8 5.5h3.4" stroke="#fff" stroke-width="1.2"/></svg></div>
        <div><h3>On-Call Staffing</h3><p>Our dedicated staffing teams answer your calls and respond as an extension of your agency</p></div>
      </div>
      <div class="service">
        <div class="service-icon"><svg viewBox="0 0 20 20"><circle cx="8" cy="6" r="3.2" fill="#fff"/><path d="M2 16c0-3.5 2.7-5.6 6-5.6 1.3 0 2.4.3 3.3.8V16z" fill="#fff"/><circle cx="14" cy="12.5" r="2.6" fill="none" stroke="#fff" stroke-width="1.3"/><path d="M15.9 14.4l2.2 2.2" stroke="#fff" stroke-width="1.4"/></svg></div>
        <div><h3>Recruiting</h3><p>Looking for the best caregivers? Let Shift Haven find qualified professionals for you.</p></div>
      </div>
      <div class="service">
        <div class="service-icon"><svg viewBox="0 0 20 20"><circle cx="10" cy="10" r="7.5" fill="#fff"/><path d="M10 5.5v9M5.5 10h9" stroke="#0677ba" stroke-width="2.4"/></svg></div>
        <div><h3>Intake</h3><p>Don't miss out on new revenue with our intake services.</p></div>
      </div>
    </div>
    <div class="banner" style="top:268px">Your agency<br>matters</div>
    <div class="block" style="top:326px;padding:0 12px 0 20px">
      <p class="dark-copy" style="margin-bottom:5px">You will benefit from dedicated implementation staff, along with the reassurance that your agency is our highest priority. Our team is committed to understanding your unique needs and providing tailored solutions that enhance your agency's operations. From seamless onboarding to ongoing support, we ensure that every aspect of our service is designed to empower you and facilitate your success.</p>
      <p class="dark-copy">With our expertise, you can focus on what truly matters: delivering exceptional care to your clients. Whether you're expanding your services or streamlining existing processes, we're here to support you every step of the way. Let us help you elevate your agency to new heights, ensuring both your staff and clients experience the best possible outcomes.</p>
    </div>
    <div class="strip navy" style="left:0;right:0"></div>
  </div>

  <div class="panel mist">
    <div class="block navy" style="top:0;height:165px;padding:20px 14px 0 14px;text-align:center">
      <h2 class="h-section" style="font-size:11.5px">US BASED <span class="accent">STAFF</span></h2>
      <div class="rule" style="width:170px;margin:6px auto 8px"></div>
      <p class="body-copy" style="font-size:8px;line-height:1.2">Shift Haven is supported by U.S.-based agents available 24/7. Real people. Real assistance. Real growth. Every single time.</p>
    </div>
    <div class="photo" style="left:12px;top:112px;width:202px;height:190px;background:linear-gradient(150deg,#0677ba,#003f82)" role="img" aria-label="Illustration of a United States map with connected people icons over a desk with hands on a tablet"></div>
    <div class="block" style="top:336px;text-align:center">
      <div style="width:30px;height:30px;border:5px solid var(--navy);margin:0 auto 12px"></div>
      <div class="brand" style="font-size:17px">Shift Haven</div>
    </div>
    <div class="strip navy" style="left:0;width:108px"></div>
    <div class="strip blue" style="left:114px;right:0"></div>
  </div>

  <div class="panel blue">
    <div class="photo" style="left:0;top:0;right:0;height:338px" role="img" aria-label="Photo of a smiling customer service agent with a headset in a bright call center"></div>
    <div class="block" style="top:360px;padding:0 14px 0 18px">
      <h2 class="h-section" style="font-size:11.5px;line-height:1.2">EMPOWER YOUR AGENCY<br>FOR EXPANSION</h2>
      <div class="rule" style="background:#fff;width:190px"></div>
      <p class="body-copy" style="font-size:7.4px">Shift Haven is not just an answering service; we provide a comprehensive solution for after-hours coverage. Say goodbye to expensive overtime costs and the risk of staff burnout.</p>
    </div>
  </div>
</section>

</body>
</html>
```